Innovative Strategic IT Solutions and Management Consulting

Looking for a fresh design idea to represent a company which specializes in innovative strategic IT solutions focusing on information assurance, enterprise content management, health information technology, web applications, strategic IT solutions and solutions architect.

KOVL...the company name means "new beginning" in Greek or the acronym for Keen-Option-Venture-Logic. We pride ourselves in understanding the client's business and needs before proposing an innovative solutions.

Innovation / Secure / Strategy - the core motto

Color: Maroon / Burgundy / Silver / White / Grey / Black

Primary focus color: Burgundy / Silver

```html
<!DOCTYPE html>
<html lang="en">
<head>
<meta charset="utf-8">
<title>KOVL – Keen-Option-Venture-Logic</title>
<link rel="stylesheet" href="https://fonts.googleapis.com/css2?family=Montserrat:wght@400;500;600&family=Roboto+Condensed:wght@400;700&family=Open+Sans:wght@400;600&display=swap">
<style>
:root{
  --burgundy:#8c0c0c;
  --burgundy-dark:#6e0000;
  --burgundy-light:#a51414;
  --ink:#111111;
  --text:#444444;
  --muted:#6a6a6a;
  --silver:#c9c9c9;
  --silver-light:#e6e6e6;
  --white:#ffffff;
}
*{margin:0;padding:0;box-sizing:border-box}
html,body{width:1200px;height:1116px;overflow:hidden;background:var(--white)}
body{position:relative;font-family:"Montserrat",Arial,sans-serif;color:var(--text)}
ul{list-style:none}
.lines{white-space:nowrap}

/* header */
.site-header{position:absolute;left:0;top:0;width:1200px;height:84px;background:var(--white);border-bottom:1px solid #eeeeee}
.brand{position:absolute;left:98px;top:22px;display:flex;align-items:center;gap:8px}
.brand-name{font-family:"Roboto Condensed",sans-serif;font-weight:700;font-size:37px;color:var(--burgundy);letter-spacing:.5px;line-height:1}
.brand-tag{font-family:"Open Sans",sans-serif;font-size:11px;line-height:13px;color:var(--burgundy);white-space:nowrap}
.main-nav a{position:absolute;top:32px;font-size:17px;color:#555;text-decoration:none;font-weight:500}
.main-nav a.current{color:var(--burgundy)}

/* hero */
.hero{position:absolute;left:0;top:85px;width:1200px;height:412px;background:linear-gradient(90deg,#e4e4e4 0%,#f4f4f4 35%,#ffffff 60%,#f6f6f6 100%)}
.hero-title{position:absolute;left:98px;top:100px;font-family:"Roboto Condensed",sans-serif;color:var(--ink);font-weight:700;white-space:nowrap}
.hero-title .l1{display:block;font-size:39px;line-height:46px}
.hero-title .l2{display:block;font-size:29px;line-height:38px;margin-top:6px}
.hero-sub{position:absolute;left:98px;top:197px;font-family:"Roboto Condensed",sans-serif;font-size:22.5px;color:var(--burgundy);white-space:nowrap}
.hero-copy{position:absolute;left:98px;top:240px;font-size:12px;line-height:21px;color:#333}
.hero-art{position:absolute;left:470px;top:10px;width:690px;height:390px;border-radius:40% 40% 30% 30%/50% 50% 30% 30%;
  background:radial-gradient(ellipse at 55% 45%,#9a9a9a 0%,#7a7a7a 12%,rgba(120,190,240,.75) 28%,rgba(250,180,70,.55) 45%,rgba(200,90,220,.25) 62%,rgba(255,255,255,0) 75%)}

/* services band */
.cta-band{position:absolute;left:0;top:497px;width:1200px;height:78px;background:linear-gradient(90deg,var(--burgundy-dark) 0%,var(--burgundy-light) 40%,var(--burgundy) 70%,var(--burgundy-dark) 100%)}
.cta-text{position:absolute;left:211px;top:21px;font-family:"Roboto Condensed",sans-serif;font-weight:700;font-size:28px;color:var(--white);text-transform:uppercase;white-space:nowrap}
.cta-text .soft{color:#d6cfcf}
.cta-arrow{position:absolute;left:682px;top:20px}
.cta-button{position:absolute;left:779px;top:17px;width:145px;height:44px;background:linear-gradient(#ffffff,#dcdcdc);border:1px solid #bbb;border-radius:3px;
  font-size:16px;font-weight:500;color:#222;letter-spacing:.5px;display:flex;align-items:center;justify-content:center}

/* info section */
.col-title{position:absolute;font-size:17px;font-weight:500;color:var(--ink);white-space:nowrap}
.tollfree-number{position:absolute;left:108px;top:660px;font-size:18px;font-weight:600;color:var(--burgundy);letter-spacing:.5px}
.tollfree-copy{position:absolute;right:964px;top:712px;text-align:right;font-size:11.5px;line-height:16.5px;color:#444;white-space:nowrap}
.tollfree-mail{position:absolute;right:964px;top:782px;text-align:right;font-size:12.5px;color:var(--burgundy)}
.col-rule{position:absolute;left:274px;top:620px;width:1px;height:262px;background:linear-gradient(#ffffff,#e2e2e2 30%,#e2e2e2 70%,#ffffff)}
.need-lead{position:absolute;left:314px;top:659px;font-size:14.5px;line-height:21px;color:var(--burgundy);white-space:nowrap}
.need-copy{position:absolute;left:316px;top:711px;font-size:11px;line-height:16.5px;color:#555;white-space:nowrap}
.consultant-photo{position:absolute;left:571px;top:626px;width:147px;height:151px;background:linear-gradient(160deg,#eef2f2 0%,#dfe7e6 45%,#b7c4b4 70%,#eceeea 100%)}
.quote-mark{position:absolute;left:320px;top:806px}
.quote-text{position:absolute;left:351px;top:815px;font-size:11px;line-height:16.5px;font-weight:600;color:var(--ink);white-space:nowrap}
.quote-author{position:absolute;right:478px;top:820px;text-align:right;font-size:12.5px;line-height:16px;white-space:nowrap}
.quote-author b{display:block;color:var(--burgundy);font-weight:600}
.quote-author span{color:#444}
.link-list{position:absolute}
.link-list li{font-size:11.5px;color:#555;height:24px;line-height:24px;padding-left:15px;position:relative;white-space:nowrap}
.link-list li::before{content:"";position:absolute;left:0;top:9px;width:4px;height:4px;border-top:1px solid #777;border-right:1px solid #777;transform:rotate(45deg)}

/* footer */
.footer-rule{position:absolute;left:98px;top:920px;width:1005px;height:1px;background:#e6e6e6}
.footer-brand{position:absolute;left:98px;top:969px;display:flex;align-items:center;gap:8px}
.footer-brand .brand-name{color:#dcdcdc;font-size:34px}
.footer-brand .brand-tag{color:#cfcfcf}
.social{position:absolute;top:1030px;width:11px;height:11px;background:#cfcfcf}
.copyright{position:absolute;left:98px;top:1069px;font-family:"Open Sans",sans-serif;font-size:10px;color:#999}
.footer-links li{font-size:12px}
.partner{position:absolute;background:#e1e1e1}
</style>
</head>
<body>

<header class="site-header">
  <div class="brand">
    <span class="brand-name">KOVL</span>
    <span class="brand-tag">Keen-Option-Venture<br>Logic</span>
  </div>
  <nav class="main-nav">
    <a class="current" style="left:539px">Home</a>
    <a style="left:627px">About Us</a>
    <a style="left:742px">Services</a>
    <a style="left:850px">Work</a>
    <a style="left:933px">Blog</a>
    <a style="left:1010px">Contact Us</a>
  </nav>
</header>

<section class="hero">
  <div class="hero-art" role="img" aria-label="Illustration of a smartphone with colourful app icons, a rainbow and blue clouds"></div>
  <h1 class="hero-title"><span class="l1">Welcome to</span><span class="l2">Keen-Option-Venture-Logic</span></h1>
  <p class="hero-sub">Strategic IT solutions and Solutions architect</p>
  <p class="hero-copy lines">Lorem Ipsum is simply dummy text of the printing and<br>typesetting industry Lorem Ipsum<br>has been the industry's</p>
</section>

<section class="cta-band">
  <p class="cta-text"><span class="soft">Click here</span> for view our services</p>
  <svg class="cta-arrow" width="56" height="38" viewBox="0 0 56 38" aria-hidden="true">
    <path d="M4 34 C8 18 22 12 38 12 L38 4 L52 16 L38 28 L38 20 C24 20 12 24 4 34 Z" fill="none" stroke="#c65a5a" stroke-width="2" stroke-linejoin="round"/>
  </svg>
  <div class="cta-button">VIEW MORE</div>
</section>

<section class="info">
  <h2 class="col-title" style="left:101px;top:623px">Call us toll free:</h2>
  <p class="tollfree-number">1 555 204 8816</p>
  <p class="tollfree-copy">Lorem Ipsum<br>Simply dummy text<br>printing and typesetting<br>industry</p>
  <p class="tollfree-mail">Contact@KOVL</p>

  <div class="col-rule"></div>

  <h2 class="col-title" style="left:314px;top:623px">Need IT solutions?</h2>
  <p class="need-lead">Simply dummy text of the<br>printing&nbsp; typesetting</p>
  <p class="need-copy">Lorem Ipsum is simply dummy text of<br>the printing and typesetting industry<br>Lorem Ipsum has been the industry's<br>standard dummy text ever</p>
  <div class="consultant-photo" role="img" aria-label="Photo of a smiling consultant in a shirt and tie holding a laptop"></div>

  <svg class="quote-mark" width="24" height="18" viewBox="0 0 24 18" aria-hidden="true">
    <path d="M5 0 H11 L6 18 H0 Z M17 0 H23 L18 18 H12 Z" fill="var(--burgundy)"/>
  </svg>
  <p class="quote-text">Lorem Ipsum is simply dummy text&nbsp; the<br>printing and typesetting istry Lorem Ipsum<br>has been the inustry's sta....</p>
  <p class="quote-author"><b>Daniel Reyes</b><span>(simply dummy)</span></p>

  <h2 class="col-title" style="left:792px;top:622px">Featured:</h2>
  <ul class="link-list" style="left:790px;top:657px">
    <li>Managed Services</li><li>Virtual Office</li><li>Starting Planning</li><li>Mobile IT</li><li>Network Security</li><li>web applications</li>
  </ul>

  <h2 class="col-title" style="left:963px;top:621px">Popular:</h2>
  <ul class="link-list" style="left:961px;top:657px">
    <li>Lorem Ipsum is simply</li><li>Dummy text of the</li><li>Typesetting</li><li>Industry. Lorem</li><li>Ipsum has been</li><li>Industry's standard</li>
  </ul>
</section>

<footer>
  <div class="footer-rule"></div>
  <div class="footer-brand">
    <span class="brand-name">KOVL</span>
    <span class="brand-tag">Keen-Option-Venture<br>Logic</span>
  </div>
  <span class="social" style="left:97px"></span>
  <span class="social" style="left:117px"></span>
  <p class="copyright">© Copyright 2014 - KOVL. All rights reserved.</p>

  <ul class="link-list footer-links" style="left:369px;top:963px">
    <li>Home</li><li>About Us</li><li>Services</li><li>Work</li><li>Blog</li>
  </ul>
  <ul class="link-list footer-links" style="left:504px;top:964px">
    <li>IT solutions</li><li>enterprise content management</li><li>health information technology</li><li>web applications</li><li>strategic IT solutions &amp; solutions architect</li>
  </ul>

  <div class="partner" style="left:821px;top:978px;width:60px;height:24px;border-radius:3px"></div>
  <div class="partner" style="left:908px;top:978px;width:86px;height:24px;border-radius:3px"></div>
  <div class="partner" style="left:1023px;top:978px;width:80px;height:24px;border-radius:3px"></div>
  <div class="partner" style="left:821px;top:1026px;width:104px;height:26px;border-radius:3px"></div>
  <div class="partner" style="left:954px;top:1024px;width:124px;height:28px;border-radius:3px"></div>
</footer>

</body>
</html>
```